Quiet Harbor is a Quiet Harbor and needs a website design.

I need a website design for my Quiet Harbor based in Singapore. I provide counseling and other related services through therapy. I website is my front face and want it to represent my personality and the name of the company itself. My company represents non judgement, compassionate and a safe environment for people to come by and talk about their issues/problems.

I want the website to be something connected to nature earth like a perfect Sanctuary. When a person sees my website i want to immediately feel a piece of calmness and peace. This is essential to me.

Target Market(s)

All age groups above 13 years of age

Industry/Entity Type

It Company

Requirements
Must have
• Not too flashy and must connect to any common man irrespective of age
Should not have
• Good calm color concept

```html
<!DOCTYPE html>
<html lang="en">
<head>
<meta charset="utf-8">
<title>Quiet Harbor</title>
<link href="https://fonts.googleapis.com/css2?family=Oswald:wght@300&family=PT+Sans:wght@400;700&family=Arimo:wght@400&display=swap" rel="stylesheet">
<style>
:root{
  --page:#f3f3f3;
  --band:#d9d9d9;
  --ink:#555;
  --blue:#9cc3d9;
  --green:#9ad0b9;
  --lime:#c3d978;
  --rose:#d4a2a2;
  --card:#e8e8e8;
  --link:#2aa3e0;
  --foot:#e6e6e6;
  --icon:#c4c4c4;
}
*{margin:0;padding:0;box-sizing:border-box}
html,body{width:1200px;height:1136px;overflow:hidden}
body{background:var(--page);font-family:Arimo,Arial,sans-serif;color:var(--ink);position:relative}
.abs{position:absolute}
.header{left:0;top:0;width:1200px;height:86px;background:#f1f1f1}
.header-band{left:0;top:86px;width:1200px;height:8px;background:var(--band)}
.logo{left:193px;top:22px;font-family:Oswald,sans-serif;font-weight:300;font-size:29px;color:#4a4a4a;letter-spacing:.2px}
.nav a{position:absolute;top:41px;font-size:14.5px;color:#4d4d4d;text-decoration:none}
.nav .active{left:454px;top:33px;width:85px;height:34px;background:var(--blue);color:#fff;border-radius:3px;text-align:center;line-height:34px;transform:skewY(-1deg)}
.hero{left:193px;top:94px;width:814px;height:363px;background:#f0f0f0;overflow:hidden}
.hero-photo{position:absolute;left:300px;top:0;width:514px;height:363px;background:linear-gradient(180deg,#dfe5ea 0%,#e6e9ec 70%,#f2f2f2 100%)}
.hero-fade{position:absolute;left:300px;top:0;width:220px;height:363px;background:linear-gradient(90deg,#f0f0f0,rgba(240,240,240,0))}
.hero h1{position:absolute;left:0;top:98px;font-family:"PT Sans",sans-serif;font-weight:700;font-size:34px;line-height:43px;color:#4e4e4e;letter-spacing:.5px}
.hero p{position:absolute;left:0;top:188px;width:360px;font-family:"PT Sans",sans-serif;font-size:12.5px;line-height:19px;color:#555}
.dots{position:absolute;left:0;top:295px;display:flex;gap:3px}
.dots span{width:16px;height:16px;border-radius:50%;border:2px solid #c3c3c3}
.dots span:first-child{border-color:var(--blue)}
.card{position:absolute;top:485px;width:193px;height:243px}
.card svg{position:absolute;left:0;top:0}
.card h3{position:absolute;left:17px;top:11px;font-size:20px;font-weight:400;color:#fff}
.card p{position:absolute;left:17px;top:84px;width:160px;font-size:12px;line-height:17.2px;color:#808080}
.card .more{position:absolute;left:131px;top:200px;width:45px;height:25px;border-radius:3px;color:#fff;font-size:12px;font-style:italic;text-align:center;line-height:25px}
h2.best{left:193px;top:748px;font-size:26px;font-weight:400;color:#4a4a4a}
.photo-frame{left:193px;top:795px;width:172px;height:160px;border:1px solid #d6d6d6;background:#fff;padding:2px}
.photo-frame div{width:100%;height:100%;background:linear-gradient(180deg,#f4f4f4,#e2dcd6)}
.best-text{left:383px;top:797px;width:310px;font-size:12.2px;line-height:17.2px;color:#555}
.best-text p+p{margin-top:17px}
.btn{position:absolute;background:var(--blue);color:#fff;font-size:12.5px;font-style:italic;text-align:center;border-radius:3px;transform:skewY(-1deg)}
h2.offer{left:707px;top:750px;font-size:20px;font-weight:400;color:#4a4a4a}
.thumb{left:707px;width:78px;height:78px;border:1px solid #d6d6d6;background:#fff;padding:2px}
.thumb div{width:100%;height:100%}
.offer-item h4{position:absolute;left:802px;font-size:14px;font-weight:400;color:var(--link)}
.offer-item p{position:absolute;left:802px;width:210px;font-size:12.3px;line-height:17.2px;color:#555}
.footer{left:0;top:1036px;width:1200px;height:100px;background:var(--foot)}
.copy{left:193px;top:1071px;font-size:14px;color:#555}
.copy-small{left:193px;top:1092px;font-size:11px;color:#666}
.follow{left:882px;top:1060px;font-size:14px;color:#555;letter-spacing:.3px}
.social{left:882px;top:1088px;display:flex;gap:8px}
.social span{width:25px;height:25px;background:var(--icon)}
</style>
</head>
<body>
<header>
  <div class="abs header"></div>
  <div class="abs header-band"></div>
  <div class="abs logo">Quiet Harbor</div>
  <nav class="nav">
    <a class="active" href="#">Home</a>
    <a href="#" style="left:560px">Company</a>
    <a href="#" style="left:657px">Services</a>
    <a href="#" style="left:752px">Careers</a>
    <a href="#" style="left:849px">Clients</a>
    <a href="#" style="left:937px">Contacts</a>
  </nav>
</header>

<section class="abs hero">
  <div class="hero-photo" role="img" aria-label="Photo of a smiling counselor with two colleagues working in the background"></div>
  <div class="hero-fade"></div>
  <h1>Lorem ipsum dolor<br>sit amet</h1>
  <p>Lorem ipsum dolor sit amet, consectetur adipiscing elit. Sed eget est neque. Nulla at arcu lectus, sed trum tellus Nam accumsan, nisi sed pharetra mattis</p>
  <div class="dots"><span></span><span></span><span></span><span></span></div>
</section>

<section class="card" style="left:193px">
  <svg width="193" height="243" viewBox="0 0 193 243">
    <path d="M10 4 Q10 0 14 0 L183 8 Q187 8 187 12 L187 160 L8 160 Z" fill="var(--blue)"/>
    <path d="M0 56 Q0 48 8 47 L178 33 Q186 33 187 41 L193 235 Q193 243 185 243 L8 243 Q0 243 0 235 Z" fill="var(--card)"/>
    <path d="M150 47 h22 a4 4 0 0 1 4 4 v12 a4 4 0 0 1 -4 4 h-14 l-6 5 v-5 h-2 a4 4 0 0 1 -4 -4 v-12 a4 4 0 0 1 4 -4z" fill="#8c8c8c"/>
    <circle cx="157" cy="58" r="1.4" fill="#fff"/><circle cx="162" cy="58" r="1.4" fill="#fff"/><circle cx="167" cy="58" r="1.4" fill="#fff"/>
  </svg>
  <h3>Support</h3>
  <p>Natoqe penatus magnis par-turient montes diculus nulla duim fusegin alesda odio morb nuncodio. gravida cursus necluctus lorenas tristique acem auctor...</p>
  <div class="more" style="background:var(--blue)">More</div>
</section>

<section class="card" style="left:400px">
  <svg width="193" height="243" viewBox="0 0 193 243">
    <path d="M10 4 Q10 0 14 0 L183 8 Q187 8 187 12 L187 160 L8 160 Z" fill="var(--green)"/>
    <path d="M0 56 Q0 48 8 47 L178 33 Q186 33 187 41 L193 235 Q193 243 185 243 L8 243 Q0 243 0 235 Z" fill="var(--card)"/>
    <circle cx="163" cy="60" r="13" fill="#9a9a9a"/>
    <path d="M155 67 Q158 52 172 52 Q170 66 155 67 Z M155 67 L168 56" fill="#fff" stroke="#9a9a9a" stroke-width="1"/>
  </svg>
  <h3>Analysis</h3>
  <p>Natoqe penatus magnis par-turient montes diculus nulla duim fusegin alesda odio morb nuncodio. gravida cursus necluctus lorenas tristique acem auctor...</p>
  <div class="more" style="background:var(--green)">More</div>
</section>

<section class="card" style="left:607px">
  <svg width="193" height="243" viewBox="0 0 193 243">
    <path d="M10 4 Q10 0 14 0 L183 8 Q187 8 187 12 L187 160 L8 160 Z" fill="var(--lime)"/>
    <path d="M0 56 Q0 48 8 47 L178 33 Q186 33 187 41 L193 235 Q193 243 185 243 L8 243 Q0 243 0 235 Z" fill="var(--card)"/>
    <circle cx="160" cy="58" r="13" fill="#8c8c8c"/>
    <path d="M151 52 q5 -3 8 1 q-1 5 -5 5 q1 5 -3 6 z M163 49 q6 2 8 8 q-4 3 -7 0 q-3 -3 -1 -8 z M160 64 q5 -1 8 1 q-3 5 -7 6 z" fill="#e8e8e8"/>
  </svg>
  <h3>Experience</h3>
  <p>Natoqe penatus magnis par-turient montes diculus nulla duim fusegin alesda odio morb nuncodio. gravida cursus necluctus lorenas tristique acem auctor...</p>
  <div class="more" style="background:var(--lime)">More</div>
</section>

<section class="card" style="left:813px">
  <svg width="193" height="243" viewBox="0 0 193 243">
    <path d="M10 4 Q10 0 14 0 L183 8 Q187 8 187 12 L187 160 L8 160 Z" fill="var(--rose)"/>
    <path d="M0 56 Q0 48 8 47 L178 33 Q186 33 187 41 L193 235 Q193 243 185 243 L8 243 Q0 243 0 235 Z" fill="var(--card)"/>
    <circle cx="160" cy="58" r="13" fill="#8c8c8c"/>
    <path d="M156 48 L164 52 L158 58 L164 66 L155 61 L160 56 Z" fill="#e8e8e8"/>
  </svg>
  <h3>Strategies</h3>
  <p>Natoqe penatus magnis par-turient montes diculus nulla duim fusegin alesda odio morb nuncodio. gravida cursus necluctus lorenas tristique acem auctor...</p>
  <div class="more" style="background:var(--rose)">More</div>
</section>

<main>
  <h2 class="abs best">Best Solutions for Growing Business</h2>
  <div class="abs photo-frame"><div role="img" aria-label="Photo of a cheerful young man giving a thumbs up"></div></div>
  <div class="abs best-text">
    <p>Magnis parturient montes diculus nulla fusegin alesda odio morb nuncodio. gravida cursus necluctus lorenas tristique acem auctor ultricies.</p>
    <p>Donec accumsan malesuada orci. Donec situmamet eros. Lorem ipsum dolor consecetuer adipiscing mauris fermentum dictum magna. Sed laoreet aliquam leo. Utellus dolor, dapibus eget, elementum velcursus eleif aenean auctor aliquam erat volutpat.</p>
  </div>
  <div class="btn" style="left:382px;top:972px;width:78px;height:28px;line-height:28px">Read More</div>

  <h2 class="abs offer">What We Offer</h2>
  <div class="abs thumb" style="top:791px"><div role="img" aria-label="Photo of a consultant on the phone" style="background:linear-gradient(180deg,#eef1f4,#c9d3dc)"></div></div>
  <div class="offer-item">
    <h4 style="top:791px">Consulting Services</h4>
    <p style="top:816px">Accusamu dolore massa fugharum quidemed rerum facilis iusto ssimos ducimus eos et ...</p>
  </div>
  <div class="abs thumb" style="top:886px"><div role="img" aria-label="Photo of a smiling woman" style="background:linear-gradient(180deg,#f2f2f2,#e6dccf)"></div></div>
  <div class="offer-item">
    <h4 style="top:886px">Regulatory Support</h4>
    <p style="top:911px">Accusamu dolore massa fugharum quidemed rerum facilis iusto ssimos ducimus eos et ...</p>
  </div>
  <div class="btn" style="left:707px;top:982px;width:78px;height:28px;line-height:28px">View All</div>
</main>

<footer>
  <div class="abs footer"></div>
  <div class="abs copy">Copyright</div>
  <div class="abs copy-small">Quiet Harbor 2013 | PRIVACY POLICY</div>
  <div class="abs follow">FOLLOW US ON</div>
  <div class="abs social"><span></span><span></span><span></span><span></span></div>
</footer>
</body>
</html>
```